6x11 Postcard for Moving Company

Must have company logo and the company slogan underneath: "The Moving Company You Can Trust And Rely On!". Must have company phone number: 858-555-0142. Must have company email, website and address:
info@haul-pivot.com
www.haul-pivot.com
4127 Penwick Lane, Suite B1,
San Diego, CA 92177
Must have company licenses listed in the following format:
CAL-T# 574318 | CA# 208751 | MC# 362940 | USDOT# 7140829

Must include the following services:
Packing - Moving - Unpacking
Loading - Unloading
Storage In Transit
Long Term Storage
Local - Long Distance
Residential - Commercial
Licensed - Insured
Free Onsite and Video Estimates

And please include the following text above or below the phone number: "Call For FREE Friendly Estimates and Advice!"

Target Market(s)

New Homes that go on sale and Home that were sold and in pending status.

Industry/Entity Type

Moving Company

Colors

Designer to choose colors to be used in the design.

Requirements
Must have
• A photo of a family on the front of the postcard. Must be looking like a real photo of the actual owner of the company with wife and 2 kids (not just a basic stock family photo). Must have Qorvix Assurance Logo and the text "Qorvix Assured". Must say/include 5 star rating on Tarnly, Qorvix, Nestplanner, Chatterwall, Pinbrook. Must include FQC A+ Accreditation Logo. Must include the Certified HaulSure Logo (see attached) and the Golden Haul Expert badege. Must have a Book Online Option. Must leave space for FMDA permit for postage. Must include the following deals: $250 Off Long Distance Moves, $50 Off Local Moves, Free Boxes (*call for details), 1 Month Storage Free. (in smaller text must say: *Offers can not be combined with other offers)

```html
<!DOCTYPE html>
<html lang="en">
<head>
<meta charset="utf-8">
<title>Haul Pivot Postcard</title>
<link href="https://fonts.googleapis.com/css2?family=Oswald:wght@600&family=Montserrat:wght@300;400;600;800&display=swap" rel="stylesheet">
<style>
:root{
  --navy:#2e3a63;
  --red:#ec1c24;
  --ink:#333842;
  --muted:#4a4f5a;
  --line:#9a9ca2;
  --stage:#b8bccb;
  --white:#ffffff;
  --stamp:#e6e6e6;
  --badge-green:#1fa44a;
  --badge-blue:#1d5f7a;
  --badge-gold:#d9a521;
  --badge-slate:#3f4f7f;
}
*{margin:0;padding:0;box-sizing:border-box}
html,body{width:1200px;height:1200px;overflow:hidden;background:var(--stage)}
.stage{position:absolute;left:0;top:0;width:1932px;height:1932px;transform:scale(.62112);transform-origin:0 0;font-family:'Montserrat',sans-serif}
.card{position:absolute;left:332px;width:1268px;height:692px;background:var(--white);overflow:hidden}
.card--front{top:170px}
.card--back{top:1070px}
.abs{position:absolute}
.brand{display:flex;align-items:center;gap:14px}
.brand__mark{width:86px;height:86px;background:var(--red)}
.brand__name{font-family:'Oswald',sans-serif;font-weight:600;font-size:46px;color:var(--white);letter-spacing:.5px}
.slogan{font-family:'Oswald',sans-serif;font-weight:600;font-size:48px;line-height:54px;color:var(--white);text-transform:uppercase}
.book-online{display:flex;align-items:center;justify-content:center;height:34px;padding:0 22px;border-radius:17px;background:var(--red);font-weight:600;font-size:16px;letter-spacing:1.5px;color:var(--white);text-transform:uppercase}
.cta{font-weight:800;font-size:43px;line-height:45px;color:var(--white);letter-spacing:1px;text-transform:uppercase}
.phone{font-weight:300;color:var(--ink);letter-spacing:1px}
.licenses{font-size:18px;color:var(--ink);letter-spacing:.5px}
.contact{display:flex;align-items:center;gap:10px;font-size:20px;color:var(--ink)}
.contact svg{flex:none}
.services-title{font-weight:600;font-size:24px;color:var(--white);letter-spacing:1px}
.services{list-style:none;font-size:16px;color:var(--muted);letter-spacing:.4px}
.services li{display:flex;align-items:center;gap:10px;height:29px}
.trust{display:flex;align-items:center;gap:14px}
.assured{display:flex;align-items:center;gap:6px}
.assured__dot{width:46px;height:46px;border-radius:50%;background:var(--badge-green)}
.assured__text{font-size:13px;font-weight:400;color:var(--ink);letter-spacing:1px;line-height:15px;text-transform:uppercase}
.accredit{width:104px;height:44px;border-radius:4px;background:var(--badge-blue)}
.seal{width:46px;height:46px;border-radius:50%}
.seal--haulsure{background:var(--badge-slate)}
.seal--golden{background:var(--badge-gold)}
.offers{list-style:none;font-size:15px;line-height:19px;color:var(--navy);font-weight:600}
.offers b{color:var(--red);font-weight:800}
.offers-note{font-size:11px;line-height:14px;color:var(--muted)}
.footer-phone{font-weight:300;font-size:40px;color:var(--white);letter-spacing:1px}
.footer-info{font-size:16px;color:var(--white);line-height:22px;letter-spacing:.3px}
.ratings{display:flex;align-items:center;gap:34px;font-size:18px}
.ratings__label{font-weight:600;font-size:15px;color:var(--navy);letter-spacing:.5px}
.ratings__label b{color:var(--red)}
.ratings__name{font-weight:600;color:var(--navy)}
.stamp{background:var(--stamp)}
.address-line{height:2px;background:var(--line)}
</style>
</head>
<body>
<div class="stage">

  <section class="card card--front">
    <svg class="abs" style="left:0;top:0" width="1268" height="692" viewBox="0 0 1268 692">
      <defs>
        <linearGradient id="famFront" x1="0" y1="0" x2="1" y2="1">
          <stop offset="0" stop-color="#b58a5e"/><stop offset=".5" stop-color="#8f9aa3"/><stop offset="1" stop-color="#6f5640"/>
        </linearGradient>
      </defs>
      <rect x="0" y="0" width="920" height="430" fill="var(--navy)"/>
      <path d="M0 470 Q0 428 50 428 L1000 428 L1000 548 L0 548 Z" fill="var(--red)"/>
      <circle cx="995" cy="265" r="284" fill="var(--red)"/>
      <circle cx="995" cy="268" r="256" fill="var(--navy)"/>
      <circle cx="995" cy="268" r="251" fill="url(#famFront)" role="img" aria-label="Photo of the owner's family lying together on a wooden floor among moving boxes"/>
    </svg>
    <div class="abs" role="img" aria-label="Mover in red cap and blue overalls pushing a hand truck stacked with boxes" style="left:450px;top:15px;width:280px;height:245px;background:linear-gradient(160deg,#3c4a78,#5f5650 60%,#2e3a63);opacity:.6;border-radius:6px"></div>
    <div class="brand abs" style="left:72px;top:120px">
      <div class="brand__mark"></div>
      <div class="brand__name">HAUL PIVOT</div>
    </div>
    <div class="slogan abs" style="left:72px;top:266px">Moving Company<br>You Can Trust And Rely On!</div>
    <div class="book-online abs" style="left:72px;top:384px">Book Online: www.haul-pivot.com</div>
    <div class="cta abs" style="left:68px;top:443px">Call For Free Friendly<br>Estimates And Advice!</div>
    <div class="phone abs" style="left:64px;top:556px;font-size:68px;line-height:76px">858-555-0142</div>
    <div class="abs" style="left:570px;top:565px;width:2px;height:56px;background:var(--ink)"></div>
    <div class="licenses abs" style="left:610px;top:587px">CAL-T# 574318 | CA# 208751 | MC# 362940 | USDOT# 7140829</div>
    <div class="contact abs" style="left:65px;top:633px">
      <svg width="34" height="34" viewBox="0 0 34 34"><circle cx="17" cy="17" r="15.5" fill="none" stroke="var(--navy)" stroke-width="2"/><rect x="10" y="12" width="14" height="10" fill="none" stroke="var(--red)" stroke-width="1.6"/><path d="M10 12 L17 18 L24 12" fill="none" stroke="var(--red)" stroke-width="1.6"/></svg>
      info@haul-pivot.com
    </div>
    <div class="contact abs" style="left:384px;top:633px">
      <svg width="34" height="34" viewBox="0 0 34 34"><circle cx="17" cy="17" r="15.5" fill="none" stroke="var(--navy)" stroke-width="2"/><circle cx="17" cy="17" r="8" fill="var(--red)"/><path d="M9 17 H25 M17 9 V25" stroke="var(--white)" stroke-width="1"/></svg>
      www.haul-pivot.com
    </div>
    <div class="contact abs" style="left:686px;top:633px">
      <svg width="34" height="34" viewBox="0 0 34 34"><circle cx="17" cy="17" r="15.5" fill="none" stroke="var(--navy)" stroke-width="2"/><path d="M17 26 C12 20 11 17 11 14 A6 6 0 0 1 23 14 C23 17 22 20 17 26 Z" fill="var(--red)"/><circle cx="17" cy="14" r="2.4" fill="var(--white)"/></svg>
      4127 Penwick Lane, Suite B1, San Diego, CA 92177
    </div>
  </section>

  <section class="card card--back">
    <svg class="abs" style="left:0;top:0" width="1268" height="692" viewBox="0 0 1268 692">
      <defs>
        <linearGradient id="famBack" x1="0" y1="0" x2="1" y2="1">
          <stop offset="0" stop-color="#d8cfc2"/><stop offset=".55" stop-color="#8ea4c4"/><stop offset="1" stop-color="#b08a66"/>
        </linearGradient>
      </defs>
      <rect x="0" y="0" width="751" height="173" fill="var(--navy)"/>
      <path d="M395 173 L751 173 L751 206 Q751 236 721 236 L395 236 Z" fill="var(--red)"/>
      <circle cx="196" cy="232" r="222" fill="var(--red)"/>
      <circle cx="188" cy="222" r="213" fill="var(--navy)"/>
      <circle cx="188" cy="222" r="209" fill="url(#famBack)" role="img" aria-label="Photo of a family unpacking boxes together in a bright living room"/>
      <path d="M0 557 L900 557 Q965 560 972 619 L0 619 Z" fill="var(--navy)"/>
    </svg>
    <div class="brand abs" style="left:430px;top:48px">
      <div class="brand__mark" style="width:70px;height:70px"></div>
      <div class="brand__name" style="font-size:36px">HAUL PIVOT</div>
    </div>
    <div class="services-title abs" style="left:438px;top:192px">OUR SERVICES</div>
    <ul class="services abs" style="left:440px;top:259px">
      <li><svg width="12" height="12" viewBox="0 0 12 12"><circle cx="6" cy="6" r="5" fill="none" stroke="var(--red)" stroke-width="1.4"/><path d="M3.5 6 L5.4 7.8 L8.6 4.2" fill="none" stroke="var(--red)" stroke-width="1.4"/></svg>Packing - Moving - Unpacking</li>
      <li><svg width="12" height="12" viewBox="0 0 12 12"><circle cx="6" cy="6" r="5" fill="none" stroke="var(--red)" stroke-width="1.4"/><path d="M3.5 6 L5.4 7.8 L8.6 4.2" fill="none" stroke="var(--red)" stroke-width="1.4"/></svg>Loading - Unloading</li>
      <li><svg width="12" height="12" viewBox="0 0 12 12"><circle cx="6" cy="6" r="5" fill="none" stroke="var(--red)" stroke-width="1.4"/><path d="M3.5 6 L5.4 7.8 L8.6 4.2" fill="none" stroke="var(--red)" stroke-width="1.4"/></svg>Storage In Transit</li>
      <li><svg width="12" height="12" viewBox="0 0 12 12"><circle cx="6" cy="6" r="5" fill="none" stroke="var(--red)" stroke-width="1.4"/><path d="M3.5 6 L5.4 7.8 L8.6 4.2" fill="none" stroke="var(--red)" stroke-width="1.4"/></svg>Long Term Storage</li>
      <li><svg width="12" height="12" viewBox="0 0 12 12"><circle cx="6" cy="6" r="5" fill="none" stroke="var(--red)" stroke-width="1.4"/><path d="M3.5 6 L5.4 7.8 L8.6 4.2" fill="none" stroke="var(--red)" stroke-width="1.4"/></svg>Local - Long Distance</li>
      <li><svg width="12" height="12" viewBox="0 0 12 12"><circle cx="6" cy="6" r="5" fill="none" stroke="var(--red)" stroke-width="1.4"/><path d="M3.5 6 L5.4 7.8 L8.6 4.2" fill="none" stroke="var(--red)" stroke-width="1.4"/></svg>Residential - Commercial</li>
      <li><svg width="12" height="12" viewBox="0 0 12 12"><circle cx="6" cy="6" r="5" fill="none" stroke="var(--red)" stroke-width="1.4"/><path d="M3.5 6 L5.4 7.8 L8.6 4.2" fill="none" stroke="var(--red)" stroke-width="1.4"/></svg>Licensed - Insured</li>
      <li><svg width="12" height="12" viewBox="0 0 12 12"><circle cx="6" cy="6" r="5" fill="none" stroke="var(--red)" stroke-width="1.4"/><path d="M3.5 6 L5.4 7.8 L8.6 4.2" fill="none" stroke="var(--red)" stroke-width="1.4"/></svg>Free Onsite and Video Estimates</li>
      <li><svg width="12" height="12" viewBox="0 0 12 12"><circle cx="6" cy="6" r="5" fill="none" stroke="var(--red)" stroke-width="1.4"/><path d="M3.5 6 L5.4 7.8 L8.6 4.2" fill="none" stroke="var(--red)" stroke-width="1.4"/></svg>Daily Intra-State Routes</li>
    </ul>
    <div class="trust abs" style="left:30px;top:484px">
      <div class="assured">
        <div class="assured__dot"></div>
        <div class="assured__text">Qorvix<br>Assured</div>
      </div>
      <div class="accredit" role="img" aria-label="FQC A+ accreditation badge"></div>
      <div class="seal seal--haulsure" role="img" aria-label="Certified HaulSure badge"></div>
      <div class="seal seal--golden" role="img" aria-label="Golden Haul Expert badge"></div>
    </div>
    <div class="stamp abs" style="left:1093px;top:89px;width:105px;height:117px"></div>
    <div class="address-line abs" style="left:809px;top:306px;width:394px"></div>
    <div class="address-line abs" style="left:809px;top:375px;width:394px"></div>
    <div class="address-line abs" style="left:809px;top:445px;width:394px"></div>
    <ul class="offers abs" style="left:809px;top:460px">
      <li><b>$250 Off</b> Long Distance Moves</li>
      <li><b>$50 Off</b> Local Moves</li>
      <li><b>Free Boxes</b> (*call for details)</li>
      <li><b>1 Month</b> Storage Free</li>
    </ul>
    <div class="offers-note abs" style="left:809px;top:538px">*Offers can not be combined with other offers</div>
    <div class="footer-phone abs" style="left:48px;top:564px">858-555-0142</div>
    <div class="footer-info abs" style="left:386px;top:566px">
      <div style="display:flex;align-items:center;gap:12px"><svg width="14" height="14" viewBox="0 0 14 14"><circle cx="7" cy="7" r="6" fill="none" stroke="var(--white)" stroke-width="1.2"/><circle cx="7" cy="7" r="3" fill="var(--red)"/></svg>info@haul-pivot.com</div>
      <div style="display:flex;align-items:center;gap:12px"><svg width="14" height="14" viewBox="0 0 14 14"><circle cx="7" cy="7" r="6" fill="none" stroke="var(--white)" stroke-width="1.2"/><circle cx="7" cy="7" r="3" fill="var(--red)"/></svg>www.haul-pivot.com</div>
    </div>
    <div class="footer-info abs" style="left:617px;top:566px;display:flex;gap:12px">
      <svg width="14" height="14" viewBox="0 0 14 14" style="margin-top:4px"><circle cx="7" cy="7" r="6" fill="none" stroke="var(--white)" stroke-width="1.2"/><circle cx="7" cy="7" r="3" fill="var(--red)"/></svg>
      <div>4127 Penwick Lane, Suite B1,<br>San Diego, CA 92177</div>
    </div>
    <div class="ratings abs" style="left:51px;top:640px">
      <span class="ratings__label"><b>5 STAR</b> RATING ON:</span>
      <span class="ratings__name">Tarnly</span>
      <span class="ratings__name">Qorvix</span>
      <span class="ratings__name">Nestplanner</span>
      <span class="ratings__name">Chatterwall</span>
      <span class="ratings__name">Pinbrook</span>
    </div>
  </section>

</div>
</body>
</html>
```